TORVEL Business Card Design

We need a business card design for a current Plastering company now moving to building and constructing new homes.
We have been in the Plastering(rendering) business for 15yrs and have made a good name with our customers for our Top Quality of work that we provide.
We would like TORVEL to be the main attraction with an image of architectural roof tops or house design within it. Blue Yellow and Black are colours we like but are willing to see other ideas.
We would like the design to be modern and communicate quality and experience.
Industry/Entity Type
Building
Contact Information for Business Card
TORVEL Building and Plastering
PO BOX 57390 Marlowe Darwin NT 0815
PH/Fax: 08 89317725 Email: torvel@quellnet.com
Dale: 0417396248 Rosa:0409273516
ABN:58 297 130 846

```html
<!DOCTYPE html>
<html lang="en">
<head>
<meta charset="utf-8">
<title>TORVEL Building and Plastering – Business Card</title>
<link rel="stylesheet" href="https://fonts.googleapis.com/css2?family=Roboto+Condensed:wght@700&family=Mulish:wght@700&display=swap">
<style>
  :root {
    --card-blue: #1461e9;
    --brand-yellow: #f0f544;
    --text-white: #ffffff;
  }
  html, body {
    margin: 0;
    padding: 0;
    width: 1200px;
    height: 741px;
    overflow: hidden;
    background: var(--card-blue);
  }
  .card {
    position: relative;
    width: 1200px;
    height: 741px;
    background: var(--card-blue);
    overflow: hidden;
  }
  .brand-name {
    position: absolute;
    left: 0;
    top: 62px;
    width: 1200px;
    margin: 0;
    text-align: center;
    font-family: "Roboto Condensed", "Arial Narrow", sans-serif;
    font-weight: 700;
    font-size: 122px;
    line-height: 1;
    letter-spacing: 4px;
    color: var(--brand-yellow);
  }
  .trade-title {
    position: absolute;
    left: 0;
    width: 1200px;
    top: 216px;
    margin: 0;
    text-align: center;
    font-family: "Roboto Condensed", "Arial Narrow", sans-serif;
    font-weight: 700;
    font-size: 66px;
    line-height: 1;
    letter-spacing: -1.5px;
    color: var(--brand-yellow);
    padding-left: 6px;
    box-sizing: border-box;
  }
  .contact-list {
    position: absolute;
    left: 0;
    width: 1200px;
    top: 316px;
    margin: 0;
    padding: 0;
    list-style: none;
    text-align: center;
    font-family: "Mulish", "Century Gothic", sans-serif;
    font-weight: 700;
    font-size: 36px;
    line-height: 43.8px;
    letter-spacing: 2.6px;
    color: var(--text-white);
  }
</style>
</head>
<body>
  <main class="card">
    <p class="brand-name">TORVEL</p>

    <h1 class="trade-title">Building &amp; Plastering</h1>

    <ul class="contact-list">
      <li class="contact-address">PO Box 57390</li>
      <li class="contact-address">Marlowe Darwin</li>
      <li class="contact-address">NT 0815</li>
      <li class="contact-phone">PH/Fax: 08 89317725</li>
      <li class="contact-email">Email: torvel@quellnet.com</li>
      <li class="contact-person">Dale: 0417396248</li>
      <li class="contact-person">Rosa: 0409273516</li>
      <li class="contact-abn">ABN: 58 297 130 846</li>
    </ul>
  </main>
</body>
</html>
```